Web Design Project for Web Agency

WHAT I NEED:
The design I need (PSD file) is for a microsite designed for employee recruitment for Brennick, a Web agency.
***Design for the 1st Page ONLY : "Manifeste"
OBJECTIVES OF THE WEBSITE:
1. To promote the agency's corporate culture and HR management principles.
2. To get people to apply on available jobs
ELEMENTS OF THE PAGE "MANIFESTE" :
1. Brennick logo (see attached files). Beside the logo must be the word "Carrières" ("Careers" in english)
***The logo is not final and there is NO branding for Brennick yet. That is why there are multiple files. So please feel free to be creative!
2. Main menu : 4 sections
Manifeste | Opportunités | Brenick | Postuler
3. Manifeste :
This page is the home page. It will present 2 main sections :
a. The agency's corporate culture :
- Title of the page is a question : "Do you embrace Brennick's corporate culture?"
- Then, presentation of the 5 corporate values, each with a title and short description
- At the end of the list of values, we want a button that says "Apply now"
b. The agency's HR management principles :
- Title of the page is a question : "Do you see yourself working at Brennick?"
- Then, presentation of the 5 Management principles, each with a title and short description
- At the end of the list of principles, we want a button that says "Apply now"
VISUAL INSPIRATION
To create each section of the "Manifeste" page, we want a design that will fit with the corporate culture:
- Brennick is BOLD
- Brennick is PROUD
- Brennick is PROFESSIONAL
- Brennick is ELEGANT
- Brennick is REFINED
We want something slick and modern. Here are some Website's that we like that can be of inspiration:
- http://www.studio-varnel.com/en/services
- http://quillmorrowlab.com/

```html
<!DOCTYPE html>
<html lang="fr">
<head>
<meta charset="utf-8">
<title>Brennick — Carrières</title>
<link href="https://fonts.googleapis.com/css2?family=Roboto+Slab:wght@300;400;700&family=Cabin:ital,wght@0,400;0,600;1,400&display=swap" rel="stylesheet">
<style>
:root{
  --paper:#f2efe8;
  --paper-dark:#e6e0d3;
  --ink:#4a4746;
  --ink-soft:#7a7673;
  --orange:#f26a1b;
  --orange-dark:#c9500c;
  --night:#1d1c1c;
  --footer:#202020;
  --ring:#e2d6c2;
  --ring-edge:#d3c4aa;
  --circle:#444243;
  --circle-edge:#c9bfae;
}
*{margin:0;padding:0;box-sizing:border-box}
html,body{width:702px;height:1200px;overflow:hidden}
body{background:var(--paper);font-family:"Cabin",sans-serif;color:var(--ink);position:relative}
.abs{position:absolute}
.slab{font-family:"Roboto Slab",serif}

/* header */
.site-header{left:0;top:0;width:702px;height:59px}
.nav-link{font-size:9px;color:var(--ink-soft);top:21px}
.brand{left:0;width:702px;top:7px;text-align:center}
.brand-name{font-family:"Roboto Slab",serif;font-weight:700;font-size:23px;color:var(--orange);line-height:26px}
.brand-tag{font-size:6.5px;letter-spacing:2px;color:var(--ink-soft);line-height:8px}
.careers-tab{left:296px;top:49px;width:110px;height:21px;background:var(--paper-dark);clip-path:polygon(6% 0,94% 0,100% 50%,94% 100%,6% 100%,0 50%);font-family:"Roboto Slab",serif;font-size:10px;line-height:21px;text-align:center;color:var(--ink);z-index:2}

/* hero */
.hero{left:0;top:59px;width:702px;height:139px;background:linear-gradient(180deg,#2b2827,#161515)}
.hero-title{left:0;top:90px;width:702px;text-align:center;font-family:"Roboto Slab",serif;font-size:17px;color:#fff}
.hero-title b{color:var(--orange);font-weight:700}
.hero-sub{left:0;top:114px;width:702px;text-align:center;font-size:10px;color:#e8e4df}

/* button */
.apply{width:125px;height:30px;display:block;text-decoration:none;border-radius:2px;background:linear-gradient(180deg,#f7812f,var(--orange) 55%,#e15a0f);box-shadow:0 2px 0 var(--orange-dark)}
.apply-label{position:absolute;left:0;top:0;width:95px;line-height:30px;text-align:center;font-family:"Roboto Slab",serif;font-weight:700;font-size:14px;color:#fff}
.apply-tick{position:absolute;right:0;top:0;width:30px;height:30px;background:rgba(0,0,0,.14)}

/* section heads */
.ribbon{height:22px;background:var(--paper-dark);clip-path:polygon(3% 0,97% 0,100% 50%,97% 100%,3% 100%,0 50%);font-family:"Roboto Slab",serif;font-weight:300;font-size:10.5px;line-height:22px;text-align:center;color:var(--ink)}
.section-title{left:0;width:702px;text-align:center;font-family:"Roboto Slab",serif;font-weight:300;font-size:21px;color:var(--ink)}
.section-title b{font-weight:700}

/* numbered circle */
.num{width:34px;height:34px;border-radius:50%;background:var(--circle);border:2px solid var(--circle-edge);color:#fff;font-family:"Roboto Slab",serif;font-weight:300;font-size:14px;line-height:30px;text-align:center}

/* timeline */
.value{width:180px}
.value h3,.principle h3{font-family:"Roboto Slab",serif;font-weight:400;font-size:10.5px;color:var(--ink);line-height:13px}
.value p,.principle p{font-size:8.3px;line-height:10.5px;color:var(--ink-soft)}
.value.left{text-align:right;left:67px}
.value.right{text-align:left;left:454px}

/* experience band */
.experience{left:0;top:577px;width:702px;height:189px;background:linear-gradient(90deg,#262525 0%,#3a3837 45%,#2a2929 75%,#1f1e1e 100%)}
.exp-head{left:90px;top:596px;width:170px;border-bottom:1px solid #6b6866;padding-bottom:3px;font-family:"Roboto Slab",serif;font-size:10px;color:#eee}
.exp-head span{float:right;font-family:"Cabin",sans-serif;font-size:5.5px;color:#aaa;margin-top:3px}
.exp-quote{left:90px;top:616px;width:170px;font-style:italic;font-size:7.3px;line-height:9.5px;color:#d3cfca}
.exp-author{left:200px;top:661px;font-size:7px;color:var(--orange)}

/* principles */
.principle{width:160px;text-align:center}
.seal{left:254px;top:1048px;width:194px;height:194px;border-radius:50%;background:var(--ring);border:7px solid var(--ring-edge)}
.seal-name{left:254px;top:1068px;width:194px;text-align:center;font-family:"Roboto Slab",serif;font-weight:700;font-size:23px;color:#eee6d6}

/* footer */
.site-footer{left:0;top:1146px;width:702px;height:54px;background:var(--footer);text-align:center}
.footer-nav{margin-top:13px;font-size:7.5px;color:#9a9693}
.footer-nav span{padding:0 7px;border-left:1px solid #555}
.footer-nav span:first-child{border-left:0}
.copyright{margin-top:7px;font-size:6px;color:#6f6c6a}
</style>
</head>
<body>

<header class="site-header abs">
  <span class="nav-link abs" style="left:100px">Manifeste</span>
  <span class="nav-link abs" style="left:168px">Opportunités</span>
  <div class="brand abs">
    <div class="brand-name">Brennick</div>
    <div class="brand-tag">AGENCE NUMÉRIQUE</div>
  </div>
  <span class="nav-link abs" style="left:510px">Brenick</span>
  <span class="nav-link abs" style="left:572px">Postuler</span>
</header>
<div class="careers-tab abs">Carrières</div>

<section class="hero abs" role="img" aria-label="Mosaic of dark team portrait photos"></section>
<h1 class="hero-title abs">The agency's <b>Corporate Culture</b> and <b>HR Management Principles.</b></h1>
<p class="hero-sub abs">Suscipit repudiandae, aptent dis? Class rhoncus odit nostrud! Torquent. Explicabo amet.</p>
<a class="apply abs" style="left:289px;top:141px" href="#"><span class="apply-label">Apply Now</span><span class="apply-tick"><svg width="30" height="30" viewBox="0 0 30 30"><path d="M9 15l4 4 8-9" fill="none" stroke="#fff" stroke-width="3" stroke-linecap="round" stroke-linejoin="round"/></svg></span></a>

<!-- corporate culture -->
<div class="ribbon abs" style="left:245px;top:220px;width:212px">The agency's corporate culture</div>
<h2 class="section-title abs" style="top:245px">Do you embrace <b>Brennick's corporate culture</b>?</h2>

<svg class="abs" style="left:0;top:290px" width="702" height="225" viewBox="0 0 702 225">
  <defs><linearGradient id="stemFade" x1="0" y1="0" x2="0" y2="1"><stop offset="0" stop-color="#cfc8bb" stop-opacity="0"/><stop offset=".08" stop-color="#d6cfc2"/></linearGradient></defs>
  <rect x="348" y="3" width="6" height="210" fill="url(#stemFade)"/>
  <path d="M344 213h14l-7 8z" fill="#d6cfc2"/>
  <g stroke="#d6cfc2" stroke-width="2">
    <line x1="274" y1="37" x2="351" y2="37"/>
    <line x1="351" y1="71" x2="431" y2="71"/>
    <line x1="274" y1="109" x2="351" y2="109"/>
    <line x1="351" y1="143" x2="431" y2="143"/>
    <line x1="274" y1="176" x2="351" y2="176"/>
  </g>
  <g fill="#e8682a" stroke="#f2efe8" stroke-width="1.5">
    <circle cx="351" cy="37" r="3.5"/><circle cx="351" cy="71" r="3.5"/><circle cx="351" cy="109" r="3.5"/><circle cx="351" cy="143" r="3.5"/><circle cx="351" cy="176" r="3.5"/>
  </g>
</svg>

<div class="num abs" style="left:257px;top:310px">01</div>
<div class="num abs" style="left:414px;top:344px">02</div>
<div class="num abs" style="left:257px;top:382px">03</div>
<div class="num abs" style="left:414px;top:416px">04</div>
<div class="num abs" style="left:257px;top:449px">05</div>

<div class="value left abs" style="top:311px"><h3>Aliqua laoreet, lobortis hendrerit</h3><p>Urna dolore imperdiet accusamus tempor! Nonummy venenatis. Aliquid! Eleifend habitasse dui curae quisque.</p></div>
<div class="value right abs" style="top:345px"><h3>Aliqua laoreet, lobortis hendrerit</h3><p>Urna dolore imperdiet accusamus tempor! Nonummy venenatis. Aliquid! Eleifend habitasse dui curae quisque.</p></div>
<div class="value left abs" style="top:383px"><h3>Aliqua laoreet, lobortis hendrerit</h3><p>Urna dolore imperdiet accusamus tempor! Nonummy venenatis. Aliquid! Eleifend habitasse dui curae quisque.</p></div>
<div class="value right abs" style="top:417px"><h3>Aliqua laoreet, lobortis hendrerit</h3><p>Urna dolore imperdiet accusamus tempor! Nonummy venenatis. Aliquid! Eleifend habitasse dui curae quisque.</p></div>
<div class="value left abs" style="top:450px"><h3>Aliqua laoreet, lobortis hendrerit</h3><p>Urna dolore imperdiet accusamus tempor! Nonummy venenatis. Aliquid! Eleifend habitasse dui curae quisque.</p></div>

<a class="apply abs" style="left:289px;top:525px" href="#"><span class="apply-label">Apply Now</span><span class="apply-tick"><svg width="30" height="30" viewBox="0 0 30 30"><path d="M9 15l4 4 8-9" fill="none" stroke="#fff" stroke-width="3" stroke-linecap="round" stroke-linejoin="round"/></svg></span></a>

<!-- people experience -->
<section class="experience abs" role="img" aria-label="Monochrome photo of colleagues working at a desk with coffee and notes"></section>
<svg class="abs" style="left:343px;top:577px" width="16" height="8"><path d="M0 0h16l-8 8z" fill="#f2efe8"/></svg>
<svg class="abs" style="left:343px;top:766px" width="16" height="8"><path d="M0 0h16l-8 8z" fill="#262525"/></svg>
<div class="exp-head abs">Peoples Experience <span>view all</span></div>
<p class="exp-quote abs">“ Orci rhoncus excepteur aut! Maxime parturient curabitur saepe quaerat ad, fringilla minima ullamcorper dolorem quaerat semper consequat</p>
<p class="exp-author abs">⟶ Marc T.B.</p>

<!-- HR principles -->
<div class="ribbon abs" style="left:203px;top:791px;width:296px">The agency's HR management principles</div>
<h2 class="section-title abs" style="top:816px">Do you see yourself <b>working at Brennick?</b></h2>

<div class="num abs" style="left:147px;top:883px">01</div>
<div class="num abs" style="left:343px;top:883px">02</div>
<div class="num abs" style="left:522px;top:883px">03</div>
<div class="num abs" style="left:147px;top:1015px">04</div>
<div class="num abs" style="left:522px;top:1015px">05</div>

<div class="principle abs" style="left:84px;top:929px"><h3>Aliqua laoreet, lobortis hendrerit</h3><p>Urna dolore imperdiet accusamus tempor! Nonummy venenatis. Aliquid! Eleifend habitasse dui curae quisque.</p></div>
<div class="principle abs" style="left:280px;top:929px"><h3>Aliqua laoreet, lobortis hendrerit</h3><p>Urna dolore imperdiet accusamus tempor! Nonummy venenatis. Aliquid! Eleifend habitasse dui curae quisque.</p></div>
<div class="principle abs" style="left:459px;top:929px"><h3>Aliqua laoreet, lobortis hendrerit</h3><p>Urna dolore imperdiet accusamus tempor! Nonummy venenatis. Aliquid! Eleifend habitasse dui curae quisque.</p></div>
<div class="principle abs" style="left:84px;top:1061px"><h3>Aliqua laoreet, lobortis hendrerit</h3><p>Urna dolore imperdiet accusamus tempor! Nonummy venenatis. Aliquid! Eleifend habitasse dui curae quisque.</p></div>
<div class="principle abs" style="left:459px;top:1061px"><h3>Aliqua laoreet, lobortis hendrerit</h3><p>Urna dolore imperdiet accusamus tempor! Nonummy venenatis. Aliquid! Eleifend habitasse dui curae quisque.</p></div>

<div class="seal abs"></div>
<div class="seal-name abs">Brennick</div>
<a class="apply abs" style="left:289px;top:1096px" href="#"><span class="apply-label">Apply Now</span><span class="apply-tick"><svg width="30" height="30" viewBox="0 0 30 30"><path d="M9 15l4 4 8-9" fill="none" stroke="#fff" stroke-width="3" stroke-linecap="round" stroke-linejoin="round"/></svg></span></a>

<footer class="site-footer abs">
  <div class="footer-nav"><span>Manifeste</span><span>Opportunités</span><span>Brenick</span><span>Postuler</span></div>
  <div class="copyright">© copyrights 2013</div>
</footer>

</body>
</html>
```